Business Card Design Project

I am community manager and social media strategist. I need a double sided business card with company logo and name. Looking for something professional, elegant but also a little bit original.

• - The logo and the colours are the company colours and a required to stay.
- The size should be: 84 x 55 mm (or 3.30 x 2.16)
- The file size should be: 1039 x 697 pixels (300 dpi)
- I'd like rounded corners. :)

Use the following contact information for the card:

Léonie Vardin
Stratégie médias sociaux / community management / édition de sites sociaux
mob. : 0687529103
leonie.vardin@postelune.fr
Twitter. : @lvardin
Skype : vardin.leonie

```html
<!DOCTYPE html>
<html lang="fr">
<head>
<meta charset="utf-8">
<title>Norvale – business card proposals</title>
<link rel="stylesheet" href="https://fonts.googleapis.com/css2?family=Barlow:wght@400;500;600;700&display=swap">
<style>
  :root {
    --board: #2b2b2b;
    --brand-blue: #1f7ac0;
    --front-light: #2a86c6;
    --front-mid: #125f9c;
    --front-dark: #0a4a80;
    --card-white: #ffffff;
    --header-grey: #efefef;
    --pattern-light: rgba(255, 255, 255, 0.28);
    --pattern-grey: #e4e4e4;
    --ink: #222222;
    --label-grey: #cfcfcf;
    --text-font: "Barlow", Arial, sans-serif;
  }
  * { box-sizing: border-box; margin: 0; padding: 0; }
  html, body { width: 1200px; height: 900px; overflow: hidden; }
  body { background: var(--board); font-family: var(--text-font); position: relative; }

  .card {
    position: absolute;
    width: 279px;
    height: 182px;
    overflow: hidden;
    box-shadow: 0 4px 10px rgba(0, 0, 0, 0.5);
  }
  .card--front {
    background: linear-gradient(120deg, var(--front-light) 0%, var(--front-mid) 45%, var(--front-dark) 100%);
  }
  .card--back { background: var(--card-white); color: var(--ink); }

  .col-1 { left: 141px; }
  .col-2 { left: 459px; }
  .col-3 { left: 780px; }
  .row-front { top: 148px; }
  .row-back { top: 374px; }

  .brand {
    position: absolute;
    left: 0; right: 0;
    top: 26px;
    display: flex;
    flex-direction: column;
    align-items: center;
    color: #fff;
  }
  .brand__dot { width: 50px; height: 50px; border-radius: 50%; background: #fff; }
  .brand__name {
    margin-top: 12px;
    font-size: 24px;
    font-weight: 700;
    letter-spacing: 1px;
    line-height: 24px;
  }

  .pattern-band { position: absolute; left: 0; right: 0; bottom: 0; }
  .pattern-band--icons {
    height: 28px;
    background: linear-gradient(90deg, transparent 10%, var(--pattern-light) 40%, var(--pattern-light) 60%, transparent 90%);
  }
  .pattern-band--scatter {
    height: 48px;
    background: linear-gradient(180deg, transparent 0%, var(--pattern-light) 100%);
  }
  .pattern-band--row { height: 26px; bottom: 4px; background: var(--pattern-light); }
  .pattern-band--row-grey { height: 24px; bottom: 4px; background: var(--pattern-grey); }
  .pattern-band--scatter-grey {
    height: 28px;
    background: linear-gradient(180deg, transparent 0%, var(--pattern-grey) 100%);
  }
  .pattern-corner {
    position: absolute;
    right: 0; bottom: 0;
    width: 120px; height: 50px;
    background: linear-gradient(120deg, transparent 20%, var(--pattern-grey) 80%);
  }

  .back-header {
    position: absolute;
    left: 0; top: 0; right: 0;
    height: 50px;
    background: linear-gradient(90deg, var(--header-grey), #f7f7f7);
    display: flex;
    align-items: center;
    gap: 6px;
    padding-left: 20px;
    color: var(--brand-blue);
  }
  .back-header__dot { width: 18px; height: 18px; border-radius: 50%; background: var(--brand-blue); }
  .back-header__name { font-size: 17px; font-weight: 700; letter-spacing: 0.5px; }

  .contact { position: absolute; left: 32px; }
  .contact--original { left: 20px; top: 75px; }
  .contact--rev1 { top: 46px; }
  .contact--rev2 { top: 35px; }
  .contact__name { font-size: 13px; font-weight: 500; color: var(--brand-blue); line-height: 15px; }
  .contact__role { font-size: 8.5px; line-height: 11px; width: 230px; margin-top: 2px; }
  .contact__list { margin-top: 12px; font-size: 8.5px; line-height: 12px; list-style: none; }
  .contact--original .contact__list { margin-top: 10px; }
  .contact__list li { display: flex; }
  .contact__label { width: 42px; }
  .contact--original .contact__label { width: 42px; }
  .contact__link { color: var(--brand-blue); }

  .label {
    position: absolute;
    top: 580px;
    width: 279px;
    text-align: center;
    font-size: 28px;
    font-weight: 400;
    color: var(--label-grey);
    letter-spacing: 1px;
  }

  .signature-brand {
    position: absolute;
    left: 0; right: 0;
    top: 742px;
    display: flex;
    flex-direction: column;
    align-items: center;
    color: #fff;
  }
  .signature-brand__dot { width: 56px; height: 56px; border-radius: 50%; background: #fff; }
  .signature-brand__name { margin-top: 8px; font-size: 24px; font-weight: 700; letter-spacing: 1px; }
</style>
</head>
<body>

  <!-- Fronts -->
  <section class="card card--front col-1 row-front">
    <div class="brand"><span class="brand__dot"></span><span class="brand__name">NORVALE</span></div>
    <div class="pattern-band pattern-band--icons" role="img" aria-label="Faint strip of social media icons"></div>
  </section>
  <section class="card card--front col-2 row-front">
    <div class="brand"><span class="brand__dot"></span><span class="brand__name">NORVALE</span></div>
    <div class="pattern-band pattern-band--scatter" role="img" aria-label="Faint scattered pattern of brand symbols"></div>
  </section>
  <section class="card card--front col-3 row-front">
    <div class="brand"><span class="brand__dot"></span><span class="brand__name">NORVALE</span></div>
    <div class="pattern-band pattern-band--row" role="img" aria-label="Faint row of repeated brand symbols"></div>
  </section>

  <!-- Backs -->
  <section class="card card--back col-1 row-back">
    <header class="back-header"><span class="back-header__dot"></span><span class="back-header__name">NORVALE</span></header>
    <div class="contact contact--original">
      <p class="contact__name">Léonie Vardin</p>
      <p class="contact__role">Stratégie médias sociaux / community management / édition de sites sociaux</p>
      <ul class="contact__list">
        <li class="contact__link"><span class="contact__label">Email</span>: leonie.vardin@postelune.fr</li>
        <li><span class="contact__label">Mobile</span>: 0687529103</li>
        <li><span class="contact__label">Twitter</span>: @lvardin</li>
        <li><span class="contact__label">Skype</span>: vardin.leonie</li>
      </ul>
    </div>
    <div class="pattern-corner" role="img" aria-label="Faint cluster of social media icons"></div>
  </section>

  <section class="card card--back col-2 row-back">
    <div class="contact contact--rev1">
      <p class="contact__name">Léonie Vardin</p>
      <p class="contact__role">Stratégie médias sociaux / community management / édition de sites sociaux</p>
      <ul class="contact__list">
        <li><span class="contact__label">Email</span>: <span class="contact__link">leonie.vardin@postelune.fr</span></li>
        <li><span class="contact__label">Mobile</span>: 0687529103</li>
        <li><span class="contact__label">Twitter</span>: @lvardin</li>
        <li><span class="contact__label">Skype</span>: vardin.leonie</li>
      </ul>
    </div>
    <div class="pattern-band pattern-band--scatter-grey" role="img" aria-label="Faint scattered pattern of brand symbols"></div>
  </section>

  <section class="card card--back col-3 row-back">
    <div class="contact contact--rev2">
      <p class="contact__name">Léonie Vardin</p>
      <p class="contact__role">Stratégie médias sociaux / community management / édition de sites sociaux</p>
      <ul class="contact__list">
        <li><span class="contact__label">Email</span>: <span class="contact__link">leonie.vardin@postelune.fr</span></li>
        <li><span class="contact__label">Mobile</span>: 0687529103</li>
        <li><span class="contact__label">Twitter</span>: @lvardin</li>
        <li><span class="contact__label">Skype</span>: vardin.leonie</li>
      </ul>
    </div>
    <div class="pattern-band pattern-band--row-grey" role="img" aria-label="Faint row of repeated brand symbols"></div>
  </section>

  <!-- Version labels -->
  <p class="label col-1">Original</p>
  <p class="label col-2">Rev. 1</p>
  <p class="label col-3">Rev. 2</p>

  <!-- Brand sign-off -->
  <div class="signature-brand"><span class="signature-brand__dot"></span><span class="signature-brand__name">NORVALE</span></div>

</body>
</html>
```